Business Card of PebbleFinch
PebbleFinch
Bright & Fun-filled
Daniel Osei, CFA
President
412 Whitmore Suite 208
Larkspur Bay, OR 92655
daniel@pebblefinch.example
pebblefinch.example

```html
<!DOCTYPE html>
<html lang="en">
<head>
<meta charset="utf-8">
<title>PebbleFinch Stationery</title>
<link href="https://fonts.googleapis.com/css2?family=Roboto:wght@400;700&display=swap" rel="stylesheet">
<style>
:root{
  --bg:#e6e6e6;
  --paper:#ffffff;
  --red:#e0262a;
  --orange:#f7a81b;
  --yellow:#fbb531;
  --ink:#333333;
  --muted:#777777;
  --faint:#f3ece2;
}
*{margin:0;padding:0;box-sizing:border-box}
html,body{width:1200px;height:684px;overflow:hidden}
body{background:var(--bg);font-family:"Roboto",Arial,sans-serif;color:var(--ink);position:relative}
.piece{position:absolute;background:var(--paper);box-shadow:0 2px 8px rgba(0,0,0,.18);overflow:hidden}
.brand{display:flex;align-items:center;gap:6px}
.brand-dot{width:14px;height:14px;border-radius:50%;background:var(--orange);flex:none}
.brand-name{font-weight:700;color:var(--red);font-size:15px;letter-spacing:-.3px;white-space:nowrap}
.swoosh{position:absolute;left:0;bottom:0;width:100%}
.faint-mark{position:absolute;background:radial-gradient(circle,var(--faint) 0%,rgba(243,236,226,0) 70%)}
.web{position:absolute;font-size:7px;color:#fff;letter-spacing:.3px;white-space:nowrap}
.small{font-size:6.5px;line-height:1.45;color:var(--muted);white-space:nowrap}

.card-front{left:28px;top:150px;width:210px;height:122px}
.card-front .brand{position:absolute;left:12px;top:14px}
.card-front .brand-name{font-size:10px}
.card-front .brand-dot{width:10px;height:10px}
.card-front .person{position:absolute;left:100px;top:16px}
.person-name{font-size:7.5px;font-weight:700;color:var(--red)}
.person-title{font-size:6.5px;color:var(--muted);margin-bottom:5px}

.card-back{left:28px;top:312px;width:210px;height:122px}
.card-back .faint-mark{left:-10px;top:10px;width:90px;height:90px}
.card-back .brand{position:absolute;left:80px;top:46px}
.card-back .brand-name{font-size:13px}

.letterhead{left:262px;top:22px;width:410px;height:640px}
.letterhead .brand{position:absolute;left:26px;top:40px}
.letterhead .brand-name{font-size:18px}
.letterhead .brand-dot{width:16px;height:16px}
.letterhead .sender{position:absolute;left:240px;top:20px}
.letterhead .faint-mark{left:20px;top:230px;width:250px;height:250px}

.envelope{left:694px;top:132px;width:480px;height:230px}
.envelope .brand{position:absolute;left:28px;top:42px}
.envelope .brand-name{font-size:20px}
.envelope .brand-dot{width:18px;height:18px}
.envelope .faint-mark{left:280px;top:10px;width:200px;height:200px}
.envelope .return{position:absolute;left:28px;bottom:26px;font-size:8px;color:var(--ink);white-space:nowrap}

.envelope-back{left:930px;top:392px;width:244px;height:170px}
.envelope-back .band{position:absolute;left:0;top:0;width:100%;height:26px;background:var(--red)}
.envelope-back .seal{position:absolute;left:112px;top:5px;width:16px;height:16px;border-radius:50%;background:var(--orange)}

.card-orange{left:700px;top:420px;width:210px;height:122px;background:var(--yellow)}
.card-orange .brand{position:absolute;left:96px;top:56px}
.card-orange .brand-name{font-size:12px;color:#fff}
.card-orange .tagline{position:absolute;left:96px;top:74px;font-size:6.5px;color:#fff;white-space:nowrap}
</style>
</head>
<body>

<section class="piece card-front">
  <div class="brand"><span class="brand-dot"></span><span class="brand-name">PebbleFinch</span></div>
  <div class="person">
    <p class="person-name">Daniel Osei, CFA</p>
    <p class="person-title">President</p>
    <p class="small">412 Whitmore Suite 208<br>Larkspur Bay, OR 92655<br>Phone 949.555.0142<br>Fax 949.555.0143<br>daniel@pebblefinch.example</p>
  </div>
  <svg class="swoosh" viewBox="0 0 210 36" height="36" preserveAspectRatio="none">
    <path d="M0 18 Q105 6 210 14 L210 36 L0 36Z" fill="var(--orange)"/>
    <path d="M0 22 Q105 10 210 18 L210 36 L0 36Z" fill="var(--red)"/>
  </svg>
  <span class="web" style="right:12px;bottom:6px">www.pebblefinch.example</span>
</section>

<section class="piece card-back">
  <div class="faint-mark" role="img" aria-label="faint decorative brand mark"></div>
  <div class="brand"><span class="brand-dot"></span><span class="brand-name">PebbleFinch</span></div>
  <svg class="swoosh" viewBox="0 0 210 30" height="30" preserveAspectRatio="none">
    <path d="M0 14 Q105 4 210 12 L210 30 L0 30Z" fill="var(--orange)"/>
    <path d="M0 18 Q105 8 210 16 L210 30 L0 30Z" fill="var(--red)"/>
  </svg>
</section>

<section class="piece letterhead">
  <div class="brand"><span class="brand-dot"></span><span class="brand-name">PebbleFinch</span></div>
  <p class="small sender">412 Whitmore Suite 208<br>Larkspur Bay, OR 92655<br><br>Toll: 800.555.0190<br>Phone: 949.555.0142<br>Fax: 949.555.0143<br>Email: daniel@pebblefinch.example</p>
  <div class="faint-mark" role="img" aria-label="faint decorative brand mark"></div>
  <svg class="swoosh" viewBox="0 0 410 50" height="50" preserveAspectRatio="none">
    <path d="M0 20 Q205 6 410 16 L410 50 L0 50Z" fill="var(--orange)"/>
    <path d="M0 25 Q205 11 410 21 L410 50 L0 50Z" fill="var(--red)"/>
  </svg>
  <span class="web" style="left:170px;bottom:9px">www.pebblefinch.example</span>
</section>

<section class="piece envelope">
  <div class="faint-mark" role="img" aria-label="faint decorative brand mark"></div>
  <div class="brand"><span class="brand-dot"></span><span class="brand-name">PebbleFinch</span></div>
  <p class="return">412 Whitmore Suite 208, Larkspur Bay, OR 92655</p>
  <svg class="swoosh" viewBox="0 0 480 80" height="80" preserveAspectRatio="none" style="bottom:auto;top:150px">
    <path d="M240 30 Q360 12 480 4 L480 30Z" fill="var(--orange)"/>
    <path d="M200 34 Q340 16 480 10 L480 40 Q340 40 200 34Z" fill="var(--red)"/>
  </svg>
  <span class="web" style="right:14px;top:176px;font-size:8px">www.pebblefinch.example</span>
</section>

<section class="piece envelope-back">
  <div class="band"></div>
  <span class="seal"></span>
  <svg style="position:absolute;left:0;top:26px" width="244" height="144" viewBox="0 0 244 144">
    <path d="M0 144 L122 60 L244 144" fill="none" stroke="#dddddd" stroke-width="1"/>
    <path d="M0 0 L122 70 L244 0" fill="none" stroke="#e4e4e4" stroke-width="1"/>
  </svg>
</section>

<section class="piece card-orange">
  <div class="brand"><span class="brand-name">PebbleFinch</span></div>
  <p class="tagline">Bright &amp; Fun-filled</p>
</section>

</body>
</html>
```